Oven Cleaning flyer design

Hi there,
I need help designing a letterbox flyer. It needs to be DL size.
I have attached a rough design made with Chat GPT.
Would like back and front, have my business colors.
Please find attached mock up of what I would roughly like.
Also find attached logo.
Thank you

Target Market(s)

Home owners over 40

Industry/Entity Type

Cleaning

Requirements
Must have
• Logo, before after of oven, brand colors

```html
<!DOCTYPE html>
<html lang="en">
<head>
<meta charset="utf-8">
<title>Gleamwork Ovens – DL Flyer</title>
<link rel="stylesheet" href="https://fonts.googleapis.com/css2?family=Montserrat:wght@400;500;700;800&family=Poppins:wght@500;600&family=Playfair+Display:ital,wght@1,500&display=swap">
<style>
:root{
  --stage:#4b4c4c;
  --paper:#ffffff;
  --teal:#4bc2c9;
  --teal-deep:#26a9b1;
  --navy:#19224d;
  --ice:#ddeff3;
  --ink:#1d2233;
}
*{box-sizing:border-box;margin:0;padding:0}
html,body{width:1189px;height:1200px;overflow:hidden;background:var(--stage)}
body{position:relative;font-family:"Montserrat",sans-serif;color:var(--ink)}
.side-label{position:absolute;top:36px;width:300px;text-align:center;color:#fff;font:800 24px "Montserrat",sans-serif;letter-spacing:9px}
.side-label.front{left:159px}
.side-label.back{left:736px}

.flyer{position:absolute;top:75px;background:var(--paper);overflow:hidden}
.flyer.front{left:68px;width:504px;height:1071px}
.flyer.back{left:625px;width:507px;height:1075px}

.brand{position:absolute;top:48px;left:0;right:0;display:flex;align-items:center;justify-content:center;gap:12px}
.brand-dot{width:54px;height:54px;border-radius:50%;background:var(--teal)}
.brand-name{font:800 33px "Montserrat",sans-serif;color:var(--teal);letter-spacing:1px}

/* front */
.hero{position:absolute;left:28px;top:152px;width:449px;height:640px;background:var(--teal);border-radius:30px 30px 0 0}
.hero-title{position:absolute;left:62px;top:178px;color:#fff;font:700 42px/48px "Montserrat",sans-serif}
.hero-copy{position:absolute;left:62px;top:280px;width:370px;color:#fff;font:500 16px/20px "Montserrat",sans-serif}
.photo{position:absolute;width:216px;height:212px;border:4px solid #fff;border-radius:24px}
.photo.dirty{background:linear-gradient(160deg,#2b2a28 0%,#1a1a1a 45%,#8a6a45 75%,#5e4a36 100%)}
.photo.clean{background:linear-gradient(160deg,#3a3c3e 0%,#151515 45%,#6e6f72 75%,#b9b6ad 100%)}
.photo.tray-dirty{background:linear-gradient(150deg,#c7b9a6 0%,#6e4a33 35%,#4b3224 70%,#7b5a3b 100%)}
.photo.tray-clean{background:linear-gradient(150deg,#8c8d8c 0%,#2b2b2b 35%,#b8b09b 70%,#d8d2c4 100%)}
.tag{position:absolute;height:39px;display:flex;align-items:center;justify-content:center;font:800 16px "Montserrat",sans-serif;letter-spacing:.5px}
.tag.before{width:87px;background:var(--teal);color:#fff;border-radius:20px 0 0 20px}
.tag.after{width:86px;background:#fff;color:var(--navy);border-radius:0 20px 20px 0}

.cta{position:absolute;background:var(--navy);text-align:center;color:#fff}
.flyer.front .cta{left:28px;top:792px;width:449px;height:189px;border-radius:0 0 30px 30px}
.flyer.back .cta{left:28px;top:807px;width:451px;height:268px;border-radius:30px 30px 0 0}
.cta-head{font:700 37px/1 "Montserrat",sans-serif;color:var(--teal)}
.cta-sub{font:700 21px/1 "Montserrat",sans-serif;margin-top:8px}
.cta-phone{display:flex;align-items:center;justify-content:center;gap:6px;font:700 45px/1 "Montserrat",sans-serif;margin-top:6px}
.cta-phone svg{width:32px;height:32px}
.web{position:absolute;height:38px;border-radius:19px;background:linear-gradient(100deg,var(--teal) 60%,#8fd9de);display:flex;align-items:center;justify-content:center;gap:8px;font:500 19px "Poppins",sans-serif;color:var(--navy)}
.web svg{width:22px;height:22px}
.tagline{position:absolute;left:0;right:0;text-align:center;font:italic 500 20px "Playfair Display",serif;color:var(--navy)}
.tagline em{color:var(--teal)}

/* back */
.why{position:absolute;left:48px;top:170px;font:700 40px/44px "Montserrat",sans-serif;color:var(--navy)}
.why span{color:var(--teal);display:block}
.why-copy{position:absolute;left:54px;top:272px;width:430px;font:400 15px/18px "Montserrat",sans-serif;color:#222}
.kitchen{position:absolute;left:0;top:352px;width:507px;height:320px;background:linear-gradient(180deg,rgba(255,255,255,0) 0%,#eceeef 25%,#e3e5e6 60%,rgba(255,255,255,0) 100%)}
.offer{position:absolute;left:34px;top:545px;width:441px;height:232px;background:var(--ice);border-radius:30px}
.offer-lead{position:absolute;left:40px;top:26px;font:500 19px "Montserrat",sans-serif;color:var(--ink)}
.offer-pct{position:absolute;left:38px;top:50px;font:800 80px/1 "Montserrat",sans-serif;color:var(--teal);letter-spacing:-3px}
.offer-pct sup{font-size:36px;vertical-align:top;position:relative;top:4px;margin-right:2px}
.offer-off{position:absolute;left:38px;top:126px;font:800 84px/1 "Montserrat",sans-serif;color:var(--navy);letter-spacing:-2px}
.offer-rule{position:absolute;left:257px;top:28px;height:184px;border-left:1.5px dashed var(--teal-deep)}
.perks{position:absolute;left:274px;top:28px;width:150px;list-style:none}
.perk{display:flex;align-items:center;gap:9px;height:60px;font:600 13px/15px "Poppins",sans-serif;color:var(--navy)}
.perk + .perk{border-top:1.5px dashed var(--teal-deep)}
.perk-icon{flex:none;width:54px;height:54px;border-radius:50%;background:var(--teal-deep);display:flex;align-items:center;justify-content:center}
.perk-icon svg{width:28px;height:28px}
</style>
</head>
<body>

<div class="side-label front">FRONT</div>
<div class="side-label back">BACK</div>

<!-- FRONT SIDE -->
<section class="flyer front">
  <div class="brand"><span class="brand-dot"></span><span class="brand-name">Gleamwork Ovens</span></div>

  <div class="hero"></div>
  <h1 class="hero-title">Bring Your Oven<br>Back to Life</h1>
  <p class="hero-copy">Professional, non-caustic oven cleaning that removes built-up grease, smoke and burnt grime-leaving your oven looking fresh again.</p>

  <div class="photo dirty" style="left:29px;top:387px" role="img" aria-label="Photo of a greasy oven interior before cleaning"></div>
  <div class="photo clean" style="left:259px;top:387px" role="img" aria-label="Photo of the same oven interior after cleaning"></div>
  <div class="photo tray-dirty" style="left:29px;top:603px" role="img" aria-label="Photo of a burnt, stained oven door glass before cleaning"></div>
  <div class="photo tray-clean" style="left:259px;top:603px" role="img" aria-label="Photo of the oven door glass shining after cleaning"></div>

  <div class="tag before" style="left:165px;top:476px">BEFORE</div>
  <div class="tag after" style="left:252px;top:476px">AFTER</div>
  <div class="tag before" style="left:165px;top:691px">BEFORE</div>
  <div class="tag after" style="left:252px;top:691px">AFTER</div>

  <div class="cta">
    <div style="padding-top:42px">
      <div class="cta-head">Call Now</div>
      <div class="cta-sub">for Fast, Professional Service</div>
      <div class="cta-phone">
        <svg viewBox="0 0 24 24" fill="none" stroke="#4bc2c9" stroke-width="1.6" stroke-linejoin="round"><path d="M6.6 2.8 9.3 6.4 7.6 8.6c1.2 2.9 3.6 5.3 6.5 6.6l2.2-1.7 3.6 2.7-1.3 3.3c-8.4.2-15.4-6.8-15.3-15.4z"/><path d="M14 3.5a7 7 0 0 1 6.5 6.5M14 6.8a3.8 3.8 0 0 1 3.2 3.2"/></svg>
        <span>0400 582 913</span>
      </div>
    </div>
  </div>
  <div class="web" style="left:73px;top:957px;width:358px">
    <svg viewBox="0 0 24 24" fill="none" stroke="#19224d" stroke-width="1.4"><circle cx="12" cy="12" r="10"/><ellipse cx="12" cy="12" rx="4.5" ry="10"/><path d="M2 12h20M4 7h16M4 17h16"/></svg>
    www.gleamworkovens.com.au
  </div>
  <p class="tagline" style="top:1010px"><em>We also clean</em> cooktops, rangehoods and BBQs</p>
</section>

<!-- BACK SIDE -->
<section class="flyer back">
  <div class="brand"><span class="brand-dot"></span><span class="brand-name">Gleamwork Ovens</span></div>

  <h2 class="why"><span>Why Choose</span>Gleamwork Ovens?</h2>
  <p class="why-copy">We’re a local family business providing professional, non-caustic oven cleaning across Sunshine Coast. Using specialized equipment and proven cleaning methods, we remove heavy grease, carbon build-up, smoke residue, restoring your oven safely and effectively.</p>

  <div class="kitchen" role="img" aria-label="Faded photo of a bright white kitchen with cooktop and oven"></div>

  <div class="offer">
    <p class="offer-lead">Mention this flyer for</p>
    <div class="offer-pct"><sup>$</sup>10%</div>
    <div class="offer-off">OFF</div>
    <div class="offer-rule"></div>
    <ul class="perks">
      <li class="perk"><span class="perk-icon"><svg viewBox="0 0 24 24" fill="none" stroke="#fff" stroke-width="1.8" stroke-linecap="round" stroke-linejoin="round"><circle cx="12" cy="12" r="8"/><path d="M8 12.3l2.7 2.7L16 9.5"/></svg></span>Reliable<br>Service</li>
      <li class="perk"><span class="perk-icon"><svg viewBox="0 0 24 24" fill="none" stroke="#fff" stroke-width="1.8" stroke-linecap="round" stroke-linejoin="round"><path d="M12 3s6 6.5 6 11a6 6 0 0 1-12 0c0-4.5 6-11 6-11z"/></svg></span>Non-Caustic<br>Cleaning</li>
      <li class="perk"><span class="perk-icon"><svg viewBox="0 0 24 24" fill="none" stroke="#fff" stroke-width="1.8" stroke-linecap="round" stroke-linejoin="round"><path d="M12 3l2.6 5.3 5.8.8-4.2 4.1 1 5.8L12 16.3 6.8 19l1-5.8L3.6 9.1l5.8-.8z"/></svg></span>Satisfaction<br>Guaranteed</li>
    </ul>
  </div>

  <div class="cta">
    <div style="padding-top:36px">
      <div class="cta-head">Call Now</div>
      <div class="cta-sub">for Fast, Professional Service</div>
      <div class="cta-phone">
        <svg viewBox="0 0 24 24" fill="none" stroke="#4bc2c9" stroke-width="1.6" stroke-linejoin="round"><path d="M6.6 2.8 9.3 6.4 7.6 8.6c1.2 2.9 3.6 5.3 6.5 6.6l2.2-1.7 3.6 2.7-1.3 3.3c-8.4.2-15.4-6.8-15.3-15.4z"/><path d="M14 3.5a7 7 0 0 1 6.5 6.5M14 6.8a3.8 3.8 0 0 1 3.2 3.2"/></svg>
        <span>0400 582 913</span>
      </div>
    </div>
    <div class="web" style="left:46px;top:154px;width:360px">
      <svg viewBox="0 0 24 24" fill="none" stroke="#19224d" stroke-width="1.4"><circle cx="12" cy="12" r="10"/><ellipse cx="12" cy="12" rx="4.5" ry="10"/><path d="M2 12h20M4 7h16M4 17h16"/></svg>
      www.gleamworkovens.com.au
    </div>
    <p class="tagline" style="top:206px;color:#fff"><em>We also clean</em> cooktops, rangehoods and BBQs</p>
  </div>
</section>

</body>
</html>
```